Digital marketing agency needs a new website design

We need a new responsive design for our website: https://brivolta.com/

Brivolta is a french digital marketing company who specializes in helping companies rank higher on Quendo search engine for their keywords in order to be more visible and have more traffic and clients.

I need you to design these 5 pages:
- Home page: https://brivolta.com
- Pricing page: https://brivolta.com/packs-backlinks/
- Contact page: https://brivolta.com/contact/
- Thank you page: https://brivolta.com/merci-temp/
- Simple page : https://brivolta.com/a-propos/

Here is a list of websites that we like their design. Use it for inspiration, but make sure it is different :

https://fenrolt.io/ (this is the one I like the most)
https://ubro.com/
http://www.garvelnest.com/
https://lumbardeau.fr/
https://www.tressaplank.com/home
https://dovermick.com/fr/
https://kalvoxa.io/
https://tramoisenet.fr/

I want a 75% color background and 25% white. You should use many bright/pastel colors like this website : https://fenrolt.io/

Keep the contact form in the website header.

Target Market(s)

small business owners

Industry/Entity Type

Digital Marketing

Number of Pages Required

5+ page

Font styles to use
Sans Serif

Colors

Designer to choose colors to be used in the design.

Requirements
Must have
• Contact form in header.
• Prominent call-to-action buttons.
• Use of at least 1 flashy color, possible to use many.
• Keep the 3 chart images.
• Keep client testimonials

```html
<!DOCTYPE html>
<html lang="fr">
<head>
<meta charset="utf-8">
<title>Brivolta – Avis clients et demande de renseignements</title>
<link rel="stylesheet" href="https://fonts.googleapis.com/css2?family=Saira:wght@400;500;600;700;800&display=swap">
<style>
  :root {
    --navy: #24245c;
    --name-blue: #1c6fc4;
    --text-grey: #3a3a4a;
    --cyan-a: #00c2f5;
    --cyan-b: #06e0f7;
    --violet-a: #8859fa;
    --violet-b: #c357f4;
    --pink-a: #ec5fc4;
    --pink-b: #f8978a;
    --magenta: #c21ef0;
    --btn-a: #7417f6;
    --btn-b: #ea1ef0;
    --white: #ffffff;
  }
  * { box-sizing: border-box; margin: 0; padding: 0; }
  html, body { width: 1200px; height: 1200px; overflow: hidden; background: var(--white); }
  body { font-family: "Saira", sans-serif; position: relative; }
  .canvas { position: absolute; inset: 0; overflow: hidden; }
  .backdrop { position: absolute; inset: 0; }

  .section-title {
    position: absolute; top: 84px; left: 0; width: 1200px; text-align: center;
    font-size: 31px; font-weight: 700; letter-spacing: 1.6px; color: var(--navy);
  }
  .carousel-arrow { position: absolute; top: 186px; width: 14px; height: 20px; }
  .carousel-arrow.prev { left: 388px; }
  .carousel-arrow.next { left: 803px; }
  .avatar {
    position: absolute; border-radius: 50%;
    background: radial-gradient(circle at 45% 40%, #9a8a7c, #4a3f38);
  }
  .avatar.side { width: 44px; height: 44px; top: 174px; box-shadow: 0 0 0 2px #2f7ff0, 0 0 10px 3px rgba(40,130,255,.6); }
  .avatar.left { left: 462px; background: radial-gradient(circle at 45% 40%, #9b9b9b, #2e2e2e); }
  .avatar.right { left: 696px; background: radial-gradient(circle at 45% 40%, #d9a27c, #6e4a2e); }
  .avatar.active { width: 68px; height: 68px; left: 566px; top: 162px; box-shadow: 0 0 0 3px #10cdf0, 0 0 14px 4px rgba(0,210,245,.6); }
  .testimonial-name {
    position: absolute; top: 239px; left: 0; width: 1200px; text-align: center;
    font-size: 12.5px; font-weight: 700; letter-spacing: .6px; color: var(--name-blue);
  }
  .testimonial-role {
    position: absolute; top: 256px; left: 0; width: 1200px; text-align: center;
    font-size: 9px; letter-spacing: .4px; color: var(--text-grey);
  }
  .testimonial-quote {
    position: absolute; top: 275px; left: 320px; width: 560px; text-align: center;
    font-size: 12.4px; line-height: 18.8px; letter-spacing: .45px; color: var(--text-grey);
  }

  .enquiry-title {
    position: absolute; left: 154px; top: 634px;
    font-size: 30px; line-height: 38px; font-weight: 700; letter-spacing: 1.8px; color: var(--white);
  }
  .enquiry-text {
    position: absolute; left: 156px; top: 723px; width: 366px;
    font-size: 12.4px; line-height: 18.8px; letter-spacing: .75px; color: var(--white);
  }

  .contact-form {
    position: absolute; left: 660px; top: 562px; width: 300px; height: 430px;
    border: 2px solid var(--white); border-radius: 4px;
    box-shadow: 0 0 10px rgba(255,255,255,.35);
    color: var(--white);
  }
  .form-kicker { position: absolute; top: 14px; width: 100%; text-align: center; font-size: 12.4px; letter-spacing: .6px; }
  .form-title { position: absolute; top: 32px; width: 100%; text-align: center; font-size: 25px; line-height: 31px; font-weight: 500; letter-spacing: 1px; }
  .field-label { position: absolute; left: 32px; font-size: 12.4px; letter-spacing: .4px; }
  .field { position: absolute; left: 18px; width: 262px; border: 2px solid var(--white); border-radius: 16px; }
  .field.email { top: 136px; height: 31px; }
  .field.site { top: 202px; height: 31px; }
  .field.message {
    top: 270px; height: 91px; border-radius: 10px; padding: 6px 12px;
    font-size: 12.2px; line-height: 18.8px; letter-spacing: .3px; color: rgba(255,255,255,.7);
  }
  .submit-button {
    position: absolute; left: 93px; top: 379px; width: 112px; height: 32px; border-radius: 16px;
    background: linear-gradient(90deg, var(--btn-a), var(--btn-b));
    font-size: 12.4px; font-weight: 700; letter-spacing: 1px; line-height: 32px; text-align: center;
  }

  .site-footer { position: absolute; left: 0; top: 1098px; width: 1200px; height: 102px; background: var(--white); }
  .footer-link { position: absolute; top: 41px; font-size: 12.4px; font-weight: 600; letter-spacing: 1px; color: var(--navy); }
  .footer-social { position: absolute; top: 41px; left: 1012px; font-size: 12px; font-weight: 600; color: var(--navy); letter-spacing: .6px; }
</style>
</head>
<body>
<div class="canvas">
  <svg class="backdrop" width="1200" height="1200" viewBox="0 0 1200 1200" aria-hidden="true">
    <defs>
      <linearGradient id="cyanFill" x1="0" y1="0" x2="1" y2="0">
        <stop offset="0" stop-color="#00b8f2"/><stop offset="1" stop-color="#07e6f7"/>
      </linearGradient>
      <linearGradient id="violetFill" x1="0" y1="0" x2="1" y2="1">
        <stop offset="0" stop-color="#8459fb"/><stop offset="1" stop-color="#c757f3"/>
      </linearGradient>
      <linearGradient id="pinkFill" x1="0" y1="0" x2="1" y2="0.3">
        <stop offset="0" stop-color="#eb5ec6"/><stop offset="1" stop-color="#f99a86"/>
      </linearGradient>
      <filter id="softBlur" x="-10%" y="-50%" width="120%" height="200%"><feGaussianBlur stdDeviation="7"/></filter>
      <clipPath id="aboveFooter"><rect x="0" y="0" width="1200" height="1098"/></clipPath>
    </defs>

    <ellipse cx="928" cy="-90" rx="150" ry="118" fill="#8a55f8"/>

    <path d="M-20 380 C90 330 150 320 260 330 S470 360 600 335 S820 300 920 380 S1060 540 1110 540 S1180 420 1230 400"
          fill="none" stroke="#bdf0fc" stroke-width="14" filter="url(#softBlur)" opacity=".75"/>

    <circle cx="228" cy="73" r="26" fill="url(#cyanFill)"/>
    <circle cx="130" cy="370" r="70" fill="url(#cyanFill)"/>
    <circle cx="1264" cy="256" r="128" fill="url(#cyanFill)"/>
    <circle cx="908" cy="386" r="16" fill="url(#cyanFill)"/>

    <ellipse cx="512" cy="1120" rx="748" ry="666" fill="url(#violetFill)" clip-path="url(#aboveFooter)"/>

    <circle cx="586" cy="557" r="37" fill="url(#pinkFill)"/>
    <circle cx="325" cy="951" r="96" fill="url(#pinkFill)"/>
    <circle cx="610" cy="898" r="14" fill="url(#pinkFill)"/>
    <circle cx="1104" cy="837" r="59" fill="url(#pinkFill)"/>
    <circle cx="486" cy="985" r="2" fill="#f48aa0"/>
    <circle cx="582" cy="1050" r="5" fill="#f48aa0"/>
  </svg>

  <h2 class="section-title">Voici Ce Qu’en Pensent Nos Clients</h2>

  <svg class="carousel-arrow prev" viewBox="0 0 14 20" aria-label="Précédent"><path d="M11 2 L3 10 L11 18" fill="none" stroke="var(--magenta)" stroke-width="1.8"/></svg>
  <svg class="carousel-arrow next" viewBox="0 0 14 20" aria-label="Suivant"><path d="M3 2 L11 10 L3 18" fill="none" stroke="var(--magenta)" stroke-width="1.8"/></svg>

  <div class="avatar side left" role="img" aria-label="Photo de profil d’un client"></div>
  <div class="avatar active" role="img" aria-label="Photo de profil d’Armand Leclos"></div>
  <div class="avatar side right" role="img" aria-label="Photo de profil d’un client"></div>

  <p class="testimonial-name">Armand Leclos</p>
  <p class="testimonial-role">Propriétaire - Leclos Média</p>
  <p class="testimonial-quote">En quelques mois, nous sommes passés en 1ere page de Quendo pour tous les mots-clés ciblés. L’agence est très professionnelle et travaille de manière méthodique. Les rapports qu’ils nous remettent chaque mois sont simples à comprendre et permettent de suivre l’avancement du projet.</p>

  <h2 class="enquiry-title">Demande de<br>Renseignements</h2>
  <p class="enquiry-text">Vous aimeriez avoir plus de renseignements ou connaître les tarifs ? Remplissez le court formulaire de prise de contact et parlez-nous de vos besoins et de vos objectifs SEO. Les tarifs des backlinks varient selon la thématique.</p>

  <form class="contact-form">
    <p class="form-kicker">Score Confiance cible 15-20</p>
    <h3 class="form-title">Renseignements<br>et Tarifs</h3>
    <span class="field-label" style="top:116px">Votre e-mail</span>
    <div class="field email"></div>
    <span class="field-label" style="top:182px">Site Web</span>
    <div class="field site"></div>
    <span class="field-label" style="top:248px">Comment pouvons-nous vous aider?</span>
    <div class="field message">J’aimerais obtenir des backlinks pour améliorer les positions de notre site sur Quendo pour nos mots-clés et générer plus de trafic.</div>
    <div class="submit-button">ENVOYER</div>
  </form>

  <footer class="site-footer">
    <span class="footer-link" style="left:156px">Accueil</span>
    <span class="footer-link" style="left:235px">Améliorer son SEO</span>
    <span class="footer-link" style="left:388px">Mon compte</span>
    <span class="footer-link" style="left:499px">Mentions légales</span>
    <span class="footer-link" style="left:641px">À propos</span>
    <span class="footer-link" style="left:731px">Contact</span>
    <span class="footer-social">Pagora</span>
  </footer>
</div>
</body>
</html>
```